R.Morton LLC Organizational Change and Development

I am starting my own company as a a senior facilitator, keynote speaker, executive coach, webinar training instructor, quality management adviser, and classroom presenter. I have taught diversity and cultural competence, organizational development, change management, leadership, organizational dynamics, team-building, accountability, negotiation, work-life balance, quality management, DISC, and hundreds of web based trainings. I have a PhD. in Counseling Psychology, MBA, B.S. in Human Development, Family Studies, and a Master’s Practitioner of Neurolinguistic Programming. My degrees and certifications give me a foundation for advising a wide variety of people, industries, and cultures at all organizational levels. I would like a design that's fun, engaging, humorous, progressive, and has a professional feel. I really like the colors burgundy wine.

Target Market(s)

corporate America

Industry/Entity Type

Training

Number of Pages Required

5+ page

Colors
eb1f26
f04a50
3176b4
33a6d7

Requirements
Must have
• my different areas of expertise - fun visuals -easy for me to use
Should not have
• something that looks stiff, too traditional or boring

```html
<!DOCTYPE html>
<html lang="en">
<head>
<meta charset="utf-8">
<title>R. Morton — Organizational Change and Development</title>
<link href="https://fonts.googleapis.com/css2?family=Roboto:wght@300;400;500&display=swap" rel="stylesheet">
<style>
  :root {
    --red: #eb1f26;
    --red-light: #f04a50;
    --red-dark: #b8161c;
    --burgundy: #8a1a22;
    --blue: #3176b4;
    --sky: #33a6d7;
    --header-bg: #fdfcf8;
    --ink: #222222;
    --body-text: #6a6a6a;
    --rule: #bdbdbd;
    --white: #ffffff;
  }
  * { box-sizing: border-box; margin: 0; padding: 0; }
  html, body { width: 1048px; height: 1200px; overflow: hidden; }
  body {
    position: relative;
    background: var(--white);
    font-family: 'Roboto', Arial, sans-serif;
    color: var(--ink);
  }

  /* Header */
  .site-header {
    position: absolute; left: 0; top: 0; width: 1048px; height: 105px;
    background: var(--header-bg);
    border-top: 3px solid #231a16;
  }
  .brand {
    position: absolute; left: 154px; top: 26px;
    font-size: 42px; font-weight: 400; color: var(--burgundy);
    letter-spacing: 1px; line-height: 48px;
  }
  .main-nav { position: absolute; top: 36px; left: 427px; display: flex; align-items: center; }
  .main-nav a {
    font-size: 12px; color: var(--ink); text-decoration: none;
    line-height: 31px; margin-right: 25px; white-space: nowrap;
  }
  .main-nav a.is-active {
    background: linear-gradient(var(--red-light), var(--red));
    color: var(--white); padding: 0 14px; border-radius: 2px; margin-right: 11px;
  }

  /* Hero */
  .hero {
    position: absolute; left: 0; top: 105px; width: 1048px; height: 463px;
    background: linear-gradient(180deg, #2a1712 0%, #1c100c 45%, #050302 100%);
    overflow: hidden;
  }
  .hero-portrait {
    position: absolute; left: 555px; top: 0; width: 330px; height: 463px;
    background: radial-gradient(ellipse at 50% 30%, #6b5848 0%, #3a2a22 40%, rgba(20,12,10,0) 75%);
  }
  .hero-title {
    position: absolute; left: 148px; top: 186px;
    font-size: 30px; font-weight: 400; color: var(--white);
  }
  .hero-subtitle {
    position: absolute; left: 148px; top: 231px;
    font-size: 20px; font-weight: 400; color: var(--white);
  }
  .hero-arrow { position: absolute; top: 193px; }
  .hero-arrow.prev { left: 60px; }
  .hero-arrow.next { left: 950px; }
  .hero-shadow {
    position: absolute; left: 60px; top: 568px; width: 928px; height: 24px;
    background: radial-gradient(ellipse at 50% 0%, rgba(0,0,0,0.22) 0%, rgba(0,0,0,0) 70%);
  }

  /* Welcome */
  .welcome-title {
    position: absolute; left: 0; top: 606px; width: 1048px; text-align: center;
    font-size: 21px; font-weight: 500; color: var(--blue);
  }
  .welcome-text {
    position: absolute; left: 148px; top: 644px; width: 752px;
    font-size: 13px; line-height: 22.4px; color: var(--body-text);
    text-align: center; font-weight: 300;
  }
  .btn-buy {
    position: absolute; left: 463px; top: 728px; width: 105px; height: 30px;
    background: linear-gradient(var(--red-light), var(--red-dark));
    border: 1px solid #9e1218; border-radius: 3px;
    color: var(--white); font-size: 10.5px; font-weight: 500;
    text-align: center; line-height: 28px; text-decoration: none;
  }
  .divider { position: absolute; left: 148px; top: 768px; width: 752px; height: 1px; background: var(--rule); }

  /* Services */
  .services-title {
    position: absolute; left: 147px; top: 797px;
    font-size: 21px; font-weight: 500; color: var(--blue);
  }
  .services-arrows { position: absolute; left: 844px; top: 799px; }
  .service-card { position: absolute; top: 840px; width: 171px; text-align: center; }
  .service-photo {
    width: 171px; height: 113px; border: 3px solid var(--white);
    box-shadow: 0 1px 4px rgba(0,0,0,0.35);
  }
  .service-name { margin-top: 22px; font-size: 13.5px; color: var(--red); font-weight: 400; }
  .service-desc { margin-top: 8px; font-size: 9.8px; line-height: 15px; color: #555; }

  /* Footer */
  .site-footer {
    position: absolute; left: 0; top: 1068px; width: 1048px; height: 132px;
    background: var(--sky); color: var(--white);
  }
  .footer-links { position: absolute; left: 151px; top: 46px; font-size: 13px; }
  .footer-links a { color: var(--white); text-decoration: none; }
  .copyright { position: absolute; left: 150px; top: 71px; font-size: 13px; }
  .follow-title { position: absolute; left: 727px; top: 32px; font-size: 13px; }
  .social-list { position: absolute; left: 728px; top: 56px; display: flex; gap: 0.5px; }
  .social-item { width: 28px; height: 28px; display: block; }
</style>
</head>
<body>

<header class="site-header">
  <div class="brand">R. MORTON</div>
  <nav class="main-nav">
    <a href="#" class="is-active">HOME</a>
    <a href="#">ABOUT US</a>
    <a href="#">SERVICES</a>
    <a href="#">COUNSELING PSYCHOLOGY</a>
    <a href="#">CONTACT US</a>
  </nav>
</header>

<section class="hero">
  <div class="hero-portrait" role="img" aria-label="Portrait of the consultant in a dark blazer, arms crossed, smiling"></div>
  <h1 class="hero-title">PhD. in Counseling Psychology</h1>
  <p class="hero-subtitle">MBA in Human Development &amp; Family Studies</p>
  <svg class="hero-arrow prev" width="30" height="60" viewBox="0 0 30 60" aria-label="Previous slide">
    <polyline points="28,2 2,30 28,58" fill="none" stroke="#ffffff" stroke-width="1.5"/>
  </svg>
  <svg class="hero-arrow next" width="30" height="60" viewBox="0 0 30 60" aria-label="Next slide">
    <polyline points="2,2 28,30 2,58" fill="none" stroke="#ffffff" stroke-width="1.5"/>
  </svg>
</section>
<div class="hero-shadow"></div>

<h2 class="welcome-title">WELCOME TO R. MORTON</h2>
<p class="welcome-text">Lorem Ipsum has been the industry's standard dummy text ever since the 1500s, when an unknown printer took a galley of type and scrambled it to make a type specimen book. It has survived not only five centuries, but also the leap into electronic typesetting, remaining essentially unchanged. It was popularised in the 1960s with the release of Letraset sheets containing Lorem Ipsum pas-</p>
<a href="#" class="btn-buy">BUY NOW</a>
<div class="divider"></div>

<h2 class="services-title">SERVICES</h2>
<svg class="services-arrows" width="58" height="22" viewBox="0 0 58 22" aria-label="Scroll services">
  <circle cx="11" cy="11" r="9.5" fill="none" stroke="#111" stroke-width="1.6"/>
  <polyline points="13,7 9,11 13,15" fill="none" stroke="#111" stroke-width="1.6"/>
  <circle cx="41" cy="11" r="9.5" fill="none" stroke="#111" stroke-width="1.6"/>
  <polyline points="39,7 43,11 39,15" fill="none" stroke="#111" stroke-width="1.6"/>
</svg>

<div class="service-card" style="left:148px">
  <div class="service-photo" role="img" aria-label="Business team meeting in a bright office" style="background:linear-gradient(160deg,#e9eef2,#b9c2c9)"></div>
  <h3 class="service-name">Executive coach</h3>
  <p class="service-desc">Lorem Ipsum is simply dummy text of the printing and typesetting industry</p>
</div>
<div class="service-card" style="left:341px">
  <div class="service-photo" role="img" aria-label="Speaker at a podium before an auditorium audience" style="background:linear-gradient(180deg,#6b4a2e,#c98a3c 55%,#3a2418)"></div>
  <h3 class="service-name">Keynote speaker</h3>
  <p class="service-desc">Lorem Ipsum is simply dummy text of the printing and typesetting industry</p>
</div>
<div class="service-card" style="left:534px">
  <div class="service-photo" role="img" aria-label="Empty classroom with desks and whiteboard" style="background:linear-gradient(180deg,#d9d6cc,#8e8a80)"></div>
  <h3 class="service-name">Classroom presenter</h3>
  <p class="service-desc">Lorem Ipsum is simply dummy text of the printing and typesetting industry</p>
</div>
<div class="service-card" style="left:727px">
  <div class="service-photo" role="img" aria-label="Computer training room with workstations" style="background:linear-gradient(180deg,#eef1f3,#a7adb2)"></div>
  <h3 class="service-name">Webinar training instructor</h3>
  <p class="service-desc">Lorem Ipsum is simply dummy text of the printing and typesetting industry</p>
</div>

<footer class="site-footer">
  <div class="footer-links"><a href="#">Privacy Policy</a> | <a href="#">Terms Conditions</a> | <a href="#">Sitemap</a> | <a href="#">Contact Us</a></div>
  <div class="copyright">Copyright © 2014&nbsp; All Rights Reserved</div>
  <div class="follow-title">FOLLOW US</div>
  <div class="social-list">
    <a href="#" class="social-item" aria-label="Feed" style="background:#f2a51c"></a>
    <a href="#" class="social-item" aria-label="Social link" style="background:#4fb4e6"></a>
    <a href="#" class="social-item" aria-label="Social link" style="background:#2c4f8f"></a>
    <a href="#" class="social-item" aria-label="Social link" style="background:#2a6fb5"></a>
    <a href="#" class="social-item" aria-label="Social link" style="background:#5bb1d6"></a>
    <a href="#" class="social-item" aria-label="Video channel" style="background:var(--red)"></a>
  </div>
</footer>

</body>
</html>
```